Course flyer - evolutive design

We want to have a nice design for our course programm.
In fact we are school language, and our course programm change approximatively each 2 weeks§.
For that we need a design that we can modify each 2 weeks (only dates change ) by ourselves.
We used to have a classical design but we want to upgrade it with a modern and attractive design.
We can have 3 versions one for each city.
We have 3 offices: Tunis, Sousse & Sfax
Attached you can find old designs

Target Market(s)

students from 16 years old till retired people 76 years old

Industry/Entity Type

Education

Font styles to use
Sans Serif

Requirements
Must have
• clear timing for courses (date, days, timing)
• prices
• Adresse (each flyer has its own adress)
• phone Number
• Cool image
Should not have
• Racism
• Violence
• Too much stuff

```html
<!DOCTYPE html>
<html lang="fr">
<head>
<meta charset="utf-8">
<title>Cours d'allemand – Sfax</title>
<link rel="stylesheet" href="https://fonts.googleapis.com/css2?family=Oswald:wght@400;500;600&family=Open+Sans:wght@400;600;700&display=swap">
<style>
  :root{
    --lime:#cddc28;
    --ink:#231f20;
    --paper:#ffffff;
    --backdrop:#7d7d7d;
    --teal:#1a8a7e;
    --orange:#ef7c45;
    --purple:#9b59b6;
  }
  *{box-sizing:border-box;margin:0;padding:0}
  html,body{width:1200px;height:801px;overflow:hidden}
  body{background:var(--backdrop);font-family:'Open Sans',sans-serif;position:relative}

  .flyer{position:absolute;top:150px;width:360px;height:500px;background:var(--paper);overflow:hidden;box-shadow:0 6px 18px rgba(0,0,0,.35)}
  .flyer--teal{left:30px;--accent:var(--teal)}
  .flyer--orange{left:420px;--accent:var(--orange)}
  .flyer--purple{left:810px;--accent:var(--purple)}

  .flyer__photo{position:absolute;inset:0 0 72px 0}
  .flyer--teal .flyer__photo{background:linear-gradient(180deg,#f1e4e6 0%,#eceaea 55%,#c7a48f 75%,#5d6f8a 100%)}
  .flyer--orange .flyer__photo{background:linear-gradient(180deg,#dfeaf5 0%,#bcd3ea 35%,#7ea04c 60%,#4e5e3a 82%,#8a6a4c 100%)}
  .flyer--purple .flyer__photo{background:linear-gradient(180deg,#d9d5ec 0%,#f2f2f4 40%,#c9d0c0 62%,#6a87a8 82%,#49546a 100%)}

  .flyer__title{position:absolute;font-family:'Oswald',sans-serif;font-weight:500;color:var(--ink);line-height:1;letter-spacing:-.5px}
  .flyer--teal .flyer__title,.flyer--purple .flyer__title{left:16px;top:22px;font-size:33px}
  .flyer--orange .flyer__title{left:168px;top:28px;font-size:31px;line-height:1.08}

  .date-badge{position:absolute;right:10px;top:14px;width:62px;height:44px;background:var(--lime);display:flex;align-items:center;padding-left:4px;font-family:'Oswald',sans-serif;color:var(--ink)}
  .date-badge__year{writing-mode:vertical-rl;transform:rotate(180deg);font-size:12px;font-weight:500;color:var(--accent);margin-right:4px}
  .date-badge__months{font-size:15px;font-weight:500;line-height:1}

  .brand{position:absolute;font-family:'Oswald',sans-serif;font-weight:500;font-size:42px;color:var(--ink);letter-spacing:-1px;display:flex;align-items:center;gap:8px}
  .brand__dot{width:14px;height:14px;border-radius:50%;background:var(--lime)}
  .flyer--teal .brand,.flyer--purple .brand{left:18px;top:150px}
  .flyer--orange .brand{left:22px;top:85px}

  .offers{position:absolute;right:0;top:72px;width:188px}
  .flyer--orange .offers{top:110px}
  .offer{margin-bottom:4px}
  .offer__name{background:var(--accent);color:#fff;font-family:'Oswald',sans-serif;font-weight:500;font-size:17px;line-height:24px;padding-left:8px}
  .offer__body{background:rgba(255,255,255,.9);padding:3px 8px 4px;font-size:8.5px;color:var(--ink);line-height:1.35}
  .offer__dates{color:var(--accent);font-weight:700;font-size:9.5px}
  .offer__hours{font-weight:700}

  .footer{position:absolute;left:0;right:0;bottom:0;height:72px;background:var(--ink);display:flex;color:#fff}
  .footer__office{width:88px;background:var(--accent);padding:8px 8px;font-size:6.5px;line-height:1.3}
  .footer__city{font-family:'Oswald',sans-serif;font-size:15px;font-weight:500;line-height:1.1}
  .footer__contact{flex:1;padding:10px 8px;font-family:'Oswald',sans-serif;font-size:9px;line-height:1.4;white-space:nowrap}
  .footer__tel{font-size:10px}
  .footer__tel strong{color:var(--lime);font-size:17px;font-weight:400}
  .footer__terms{width:100px;padding:8px 6px 0 0;font-size:5.4px;line-height:1.25}
</style>
</head>
<body>

<article class="flyer flyer--teal">
  <div class="flyer__photo" role="img" aria-label="Photo de jeunes étudiants assis devant un mur de briques blanches"></div>
  <h1 class="flyer__title">COURS D'ALLEMAND</h1>
  <div class="date-badge"><span class="date-badge__year">2016</span><span class="date-badge__months">MAI<br>JUIN</span></div>
  <div class="brand">lumora<span class="brand__dot"></span></div>
  <section class="offers">
    <div class="offer"><div class="offer__name">SUPER INTENSIF</div><div class="offer__body"><div class="offer__dates">DU 30 MAI AU 10 JUIN 2016</div>Du Lundi au Vendredi<div class="offer__hours">9:00 À 13:30 &amp; 13:30 À 18:00</div>390 dt.</div></div>
    <div class="offer"><div class="offer__name">INTENSIF</div><div class="offer__body"><div class="offer__dates">DU 30 MAI AU 10 JUIN 2016</div>Du Lundi au Vendredi<div class="offer__hours">9:00 À 13:30 &amp; 13:30 À 18:00</div>350 dt.</div></div>
    <div class="offer"><div class="offer__name">EXTENSIF</div><div class="offer__body"><div class="offer__dates">DU 30 MAI AU 10 JUIN 2016</div>Du Lundi au Vendredi<div class="offer__hours">9:00 À 13:30 &amp; 13:30 À 18:00</div>340 dt.</div></div>
  </section>
  <footer class="footer">
    <div class="footer__office"><div class="footer__city">SFAX</div>Avenue des Palmiers<br>Rue Ibn Khaldoun<br>Immeuble Nour<br>(5eme etage)</div>
    <div class="footer__contact"><div class="footer__tel">TEL : <strong>+216 70 123 456</strong></div>CONTACT-SFAX@LUMORA-LANGUES.ORG<br>WWW.LUMORA-LANGUES.ORG</div>
    <p class="footer__terms">Toute inscription doit impérativement se faire au plus tard une semaine avant le début des cours. Nombre minimum de 4 participants requis. L'horaire des cours est susceptible d'être modifié. Prix par module 340 TND.</p>
  </footer>
</article>

<article class="flyer flyer--orange">
  <div class="flyer__photo" role="img" aria-label="Photo d'un groupe d'étudiants assis sur un banc dans un parc sous un ciel bleu"></div>
  <h1 class="flyer__title">COURS<br>D'ALLEMAND</h1>
  <div class="date-badge"><span class="date-badge__year">2016</span><span class="date-badge__months">MAI<br>JUIN</span></div>
  <div class="brand">lumora<span class="brand__dot"></span></div>
  <section class="offers">
    <div class="offer"><div class="offer__name">SUPER INTENSIF</div><div class="offer__body"><div class="offer__dates">DU 30 MAI AU 10 JUIN 2016</div>Du Lundi au Vendredi<div class="offer__hours">9:00 À 13:30 &amp; 13:30 À 18:00</div>390 dt.</div></div>
    <div class="offer"><div class="offer__name">INTENSIF</div><div class="offer__body"><div class="offer__dates">DU 30 MAI AU 10 JUIN 2016</div>Du Lundi au Vendredi<div class="offer__hours">9:00 À 13:30 &amp; 13:30 À 18:00</div>350 dt.</div></div>
    <div class="offer"><div class="offer__name">EXTENSIF</div><div class="offer__body"><div class="offer__dates">DU 30 MAI AU 10 JUIN 2016</div>Du Lundi au Vendredi<div class="offer__hours">9:00 À 13:30 &amp; 13:30 À 18:00</div>340 dt.</div></div>
  </section>
  <footer class="footer">
    <div class="footer__office"><div class="footer__city">SFAX</div>Avenue des Palmiers<br>Rue Ibn Khaldoun<br>Immeuble Nour<br>(5eme etage)</div>
    <div class="footer__contact"><div class="footer__tel">TEL : <strong>+216 70 123 456</strong></div>CONTACT-SFAX@LUMORA-LANGUES.ORG<br>WWW.LUMORA-LANGUES.ORG</div>
    <p class="footer__terms">Toute inscription doit impérativement se faire au plus tard une semaine avant le début des cours. Nombre minimum de 4 participants requis. L'horaire des cours est susceptible d'être modifié. Prix par module 340 TND.</p>
  </footer>
</article>

<article class="flyer flyer--purple">
  <div class="flyer__photo" role="img" aria-label="Photo d'étudiants souriants avec sacs à dos et cahiers sur un campus"></div>
  <h1 class="flyer__title">COURS D'ALLEMAND</h1>
  <div class="date-badge"><span class="date-badge__year">2016</span><span class="date-badge__months">MAI<br>JUIN</span></div>
  <div class="brand">lumora<span class="brand__dot"></span></div>
  <section class="offers">
    <div class="offer"><div class="offer__name">SUPER INTENSIF</div><div class="offer__body"><div class="offer__dates">DU 30 MAI AU 10 JUIN 2016</div>Du Lundi au Vendredi<div class="offer__hours">9:00 À 13:30 &amp; 13:30 À 18:00</div>390 dt.</div></div>
    <div class="offer"><div class="offer__name">INTENSIF</div><div class="offer__body"><div class="offer__dates">DU 30 MAI AU 10 JUIN 2016</div>Du Lundi au Vendredi<div class="offer__hours">9:00 À 13:30 &amp; 13:30 À 18:00</div>350 dt.</div></div>
    <div class="offer"><div class="offer__name">EXTENSIF</div><div class="offer__body"><div class="offer__dates">DU 30 MAI AU 10 JUIN 2016</div>Du Lundi au Vendredi<div class="offer__hours">9:00 À 13:30 &amp; 13:30 À 18:00</div>340 dt.</div></div>
  </section>
  <footer class="footer">
    <div class="footer__office"><div class="footer__city">SFAX</div>Avenue des Palmiers<br>Rue Ibn Khaldoun<br>Immeuble Nour<br>(5eme etage)</div>
    <div class="footer__contact"><div class="footer__tel">TEL : <strong>+216 70 123 456</strong></div>CONTACT-SFAX@LUMORA-LANGUES.ORG<br>WWW.LUMORA-LANGUES.ORG</div>
    <p class="footer__terms">Toute inscription doit impérativement se faire au plus tard une semaine avant le début des cours. Nombre minimum de 4 participants requis. L'horaire des cours est susceptible d'être modifié. Prix par module 340 TND.</p>
  </footer>
</article>

</body>
</html>
```